Business Card Designs

Looking to design a 3.5" x 2" standard business card for our employees.
The design needs to be sleek, simple, and modern. We would like our logo (attached) to be incorporated, but not in that colour, rather an outline of the logo in either gold or silver (whichever looks better).

Modern and Simple is what we are looking for, but be creative in incorporating the logo.

```html
<!DOCTYPE html>
<html lang="en">
<head>
<meta charset="utf-8">
<title>Harbourline Suites – Business Card</title>
<link href="https://fonts.googleapis.com/css2?family=Roboto:wght@400;500&display=swap" rel="stylesheet">
<style>
  :root {
    --page-bg: #d8d5d3;
    --panel-black: #000000;
    --silver: #c8c8c8;
    --card-light: #f1f0f0;
    --card-light-edge: #e3e2e2;
    --ink: #111111;
    --divider: #1a1a1a;
    --gap-white: #ffffff;
  }
  * { margin: 0; padding: 0; box-sizing: border-box; }
  html, body {
    width: 1200px;
    height: 900px;
    overflow: hidden;
    background: var(--page-bg);
    font-family: "Roboto", sans-serif;
  }
  .card {
    position: absolute;
    left: 110px;
    top: 147px;
    width: 980px;
    height: 605px;
    display: flex;
    box-shadow: 0 10px 30px rgba(0,0,0,0.18);
  }
  .card__brand-panel {
    width: 442px;
    height: 100%;
    background: var(--panel-black);
    display: flex;
    flex-direction: column;
    align-items: center;
    justify-content: center;
  }
  .brand-name {
    color: var(--silver);
    font-weight: 500;
    font-size: 30px;
    letter-spacing: 5px;
    text-align: center;
    line-height: 1.35;
  }
  .card__gap { width: 8px; background: var(--gap-white); }
  .card__bar { width: 9px; background: var(--panel-black); }
  .card__details {
    flex: 1;
    background: radial-gradient(ellipse at 40% 50%, var(--card-light) 0%, var(--card-light-edge) 100%);
    padding: 138px 0 0 66px;
    color: var(--ink);
  }
  .person-name {
    font-weight: 500;
    font-size: 40px;
    line-height: 1;
    letter-spacing: 0.2px;
  }
  .person-title {
    font-size: 27px;
    line-height: 1.2;
    margin-top: 4px;
  }
  .rule {
    width: 87px;
    height: 2px;
    background: var(--divider);
    margin: 26px 0 24px;
  }
  .contact-list { list-style: none; }
  .contact-item {
    display: flex;
    align-items: center;
    gap: 10px;
    font-size: 28px;
    line-height: 36px;
    white-space: nowrap;
  }
  .contact-item svg { width: 27px; height: 27px; flex: none; }
  .address {
    font-size: 28px;
    line-height: 36px;
    font-style: normal;
    white-space: nowrap;
  }
</style>
</head>
<body>
  <div class="card">
    <section class="card__brand-panel">
      <p class="brand-name">HARBOURLINE<br>SUITES</p>
    </section>
    <div class="card__gap"></div>
    <div class="card__bar"></div>
    <section class="card__details">
      <h1 class="person-name">DANIEL CARTER</h1>
      <p class="person-title">Managing Director</p>
      <div class="rule"></div>
      <ul class="contact-list">
        <li class="contact-item">
          <svg viewBox="0 0 24 24" aria-hidden="true"><path fill="#111" d="M6.6 10.8a15.1 15.1 0 0 0 6.6 6.6l2.2-2.2c.3-.3.7-.4 1-.2 1.1.4 2.3.6 3.6.6.6 0 1 .4 1 1V20c0 .6-.4 1-1 1A17 17 0 0 1 3 4c0-.6.4-1 1-1h3.5c.6 0 1 .4 1 1 0 1.3.2 2.5.6 3.6.1.3 0 .7-.2 1z"/><path fill="none" stroke="#111" stroke-width="1.6" d="M14 3.5a6.5 6.5 0 0 1 6.5 6.5M14 7a3 3 0 0 1 3 3"/></svg>
          <span>044-987 210 365</span>
        </li>
        <li class="contact-item">
          <svg viewBox="0 0 24 24" aria-hidden="true"><rect x="2" y="5" width="20" height="14" fill="#111"/><path d="M2.5 5.5 12 13l9.5-7.5" fill="none" stroke="#f1f0f0" stroke-width="1.6"/></svg>
          <span>hello@harbourline.com</span>
        </li>
        <li class="contact-item">
          <svg viewBox="0 0 24 24" aria-hidden="true"><g fill="none" stroke="#111" stroke-width="1.6"><circle cx="12" cy="12" r="9.5"/><ellipse cx="12" cy="12" rx="4.2" ry="9.5"/><path d="M2.5 12h19M4 7h16M4 17h16"/></g></svg>
          <span>www.harbourlinesuites.com</span>
        </li>
      </ul>
      <div class="rule"></div>
      <address class="address">188 Quayside Avenue, Unit 4<br>61730, Northbay</address>
    </section>
  </div>
</body>
</html>
```